'Wedding Business" Business Card Design

dj services for weddings and parties, uplighting, event planning, day of coordination for weddings, photography for weddings and other events.

Would like raised print and metallic also if possible. Elegant design, yet modern. This is a wedding business and should describe our goals and main services - DJ/lighting, wedding and event planning, photography. slogan "Simply Incredible, Incredibly simple" or "Your Dreams. Our Experience. The Perfect Match" Our goal is to provide multiple services to make it easier for the bride and groom almost like a one stop shop. Feel free to use the slogan or leave it out , we just want to really stand out against the competition. You can also get more info on our website www.bluelarkproductions.com - we are working to get the bluelarkct.com site pointed to our current site!

there should be 2 files attached, if they did not go through please email events@bluelarkct.com or bluelarkproductions@mailbox.test
Updates

Thank you all for your help, we have decided what we like but would like to make some changes, we need to order these asap so please let us know if you can help.

Reason: Wasn't able to pick it out in time! So Sorry but we know what we want!!

Industry/Entity Type

Business

Contact Information for Business Card

Trevor and Mallory Quenby
555-318-2746
555-207-4831
Blue Lark Productions, Events, & Photography
EMAIL:Events@BlueLarkCT.com
www.bluelarkct.com

```html
<!DOCTYPE html>
<html lang="en">
<head>
<meta charset="utf-8">
<title>Blue Lark Productions — Business Card</title>
<link href="https://fonts.googleapis.com/css2?family=Merienda:wght@400&display=swap" rel="stylesheet">
<style>
  :root {
    --page: #e9e6e1;
    --card-black: #030303;
    --card-blue: #35409c;
    --blue-rule: #2a3290;
    --text-white: #f4f4f6;
    --logo-silver: #d9dbe2;
    --shadow: rgba(0, 0, 0, 0.28);
  }
  * { box-sizing: border-box; margin: 0; padding: 0; }
  html, body {
    width: 1200px;
    height: 848px;
    overflow: hidden;
    background: var(--page);
    font-family: "Merienda", cursive;
  }
  .sheet {
    width: 1200px;
    height: 848px;
    display: flex;
    align-items: center;
    justify-content: center;
    gap: 44px;
  }
  .card {
    width: 536px;
    height: 306px;
    background: var(--card-black);
    box-shadow: 0 10px 26px var(--shadow);
    position: relative;
    overflow: hidden;
    color: var(--text-white);
  }

  /* Contact side */
  .card--contact { display: flex; }
  .brand-panel {
    width: 44%;
    display: flex;
    align-items: center;
    justify-content: center;
  }
  .info-panel {
    flex: 1;
    background: var(--card-blue);
    border-left: 4px solid var(--blue-rule);
    padding: 42px 26px 30px 34px;
    display: flex;
    flex-direction: column;
  }
  .owners {
    font-size: 19px;
    line-height: 1.2;
    text-align: center;
  }
  .contact-list {
    list-style: none;
    margin-top: 46px;
    font-size: 13px;
    line-height: 1.55;
    text-align: center;
  }

  /* Brand wordmark stand-in */
  .wordmark {
    display: flex;
    align-items: center;
    gap: 10px;
    color: var(--logo-silver);
    font-size: 36px;
    line-height: 1;
  }
  .wordmark__dot {
    width: 12px;
    height: 12px;
    border-radius: 50%;
    background: var(--card-blue);
    flex: none;
  }

  /* Tagline side */
  .card--tagline {
    display: flex;
    flex-direction: column;
    align-items: center;
    justify-content: space-between;
    padding: 64px 24px 30px;
  }
  .card--tagline .wordmark { font-size: 42px; }
  .tagline {
    font-size: 17px;
    letter-spacing: 0.5px;
    text-align: center;
  }
</style>
</head>
<body>
  <main class="sheet">
    <section class="card card--contact" aria-label="Business card, contact side">
      <div class="brand-panel">
        <div class="wordmark"><span class="wordmark__dot"></span><span>Blue Lark</span></div>
      </div>
      <div class="info-panel">
        <p class="owners">Trevor and Mallory Quenby</p>
        <ul class="contact-list">
          <li>P : 555-318-2746</li>
          <li>P : 555-207-4831</li>
          <li>www.bluelarkct.com</li>
          <li>Events@BlueLarkCT.com</li>
        </ul>
      </div>
    </section>

    <section class="card card--tagline" aria-label="Business card, brand side">
      <div class="wordmark"><span class="wordmark__dot"></span><span>Blue Lark</span></div>
      <p class="tagline">Blue Lark Productions, Events, &amp; Photography</p>
    </section>
  </main>
</body>
</html>
```